Bluefinch Painting needs a Website

We need a website built for a Painting company I own, we mainly do residential painting, but don't want to be limited to that.

Need to have estimate request form.
Need pic's of past projects

I like the look of the website for http://www.harborline-painters.example
& "Thistledown Property inspections"

My logo that was designed here on ArtHive on the front page

I would like one of the houses I downloaded as part of the background
of the front page.

Target Market(s)

Home owners

Industry/Entity Type

Painting

Number of Pages Required

1 page

Font styles to use
Serif

Requirements
Must have
• Estimate request form for home owners to fill out -
• Name:
• Phone Number:
• Address:
• E-mail:
• Painting project description:
• And my info to:
• My phone number: (555) 318-7764
• My web address bluefinchpainting.example
Nice to have
• My logo that was designed here on ArtHive

```html
<!DOCTYPE html>
<html lang="en">
<head>
<meta charset="utf-8">
<title>Bluefinch Painting – Get an Estimate</title>
<link href="https://fonts.googleapis.com/css2?family=Montserrat:wght@400;500;600;700&family=Open+Sans:ital,wght@0,400;0,700;1,400&display=swap" rel="stylesheet">
<style>
  :root {
    --backdrop: #545454;
    --hero-deep: #142c5c;
    --hero-mid: #1f3f78;
    --accent: #2aa3d1;
    --accent-dark: #1a6f96;
    --ink: #333a40;
    --field-line: #8a8a8a;
    --field-label: #666;
    --paper: #ececec;
    --white: #ffffff;
    --footer: #000000;
  }
  * { box-sizing: border-box; margin: 0; padding: 0; }
  html, body { width: 1200px; height: 1000px; overflow: hidden; }
  body { background: var(--backdrop); font-family: "Montserrat", sans-serif; position: relative; }

  .page { position: absolute; left: 228px; top: 17px; width: 743px; height: 966px; background: var(--paper); overflow: hidden; }

  .hero { position: absolute; left: 0; top: 0; width: 743px; height: 417px;
    background: radial-gradient(ellipse at 55% 55%, var(--hero-mid) 0%, var(--hero-deep) 75%); }
  .brand { position: absolute; display: flex; align-items: center; gap: 6px; color: var(--white); font-weight: 600; letter-spacing: .04em; }
  .brand-mark { width: 14px; height: 14px; background: var(--white); }
  .hero .brand { left: 40px; top: 16px; font-size: 12px; }
  .nav { position: absolute; right: 40px; top: 18px; display: flex; gap: 18px; list-style: none; }
  .nav li { color: var(--white); font-size: 8px; font-weight: 600; }
  .hero-frame { position: absolute; left: 202px; top: 169px; width: 339px; height: 75px; border: 2px solid var(--white);
    display: flex; align-items: center; justify-content: center; color: var(--white); font-size: 33px; font-weight: 600; letter-spacing: -.01em; }
  .hero-lead { position: absolute; left: 0; width: 743px; top: 263px; text-align: center; color: var(--white);
    font-size: 11.5px; line-height: 14px; letter-spacing: .06em; text-transform: uppercase; }
  .scroll-down { position: absolute; left: 358px; top: 377px; }

  .band { position: absolute; left: 0; top: 417px; width: 743px; height: 77px; background: var(--accent); text-align: center; }
  .band h1 { margin-top: 20px; font-size: 21px; font-weight: 600; color: var(--ink); }
  .band p { margin-top: 3px; font-family: "Open Sans", sans-serif; font-style: italic; font-size: 7px; color: var(--white); }

  .contact-row { position: absolute; left: 178px; top: 528px; display: flex; align-items: center; gap: 7px; }
  .dot { width: 18px; height: 18px; border-radius: 50%; background: var(--accent); display: flex; align-items: center; justify-content: center; }
  .contact-row span { font-size: 8px; color: var(--accent); font-weight: 500; margin-left: 3px; }

  .field { position: absolute; border: 1px solid var(--field-line); font-size: 7px; font-weight: 500; color: var(--field-label);
    padding: 8px 10px; text-transform: uppercase; }
  .f-name { left: 178px; top: 561px; width: 386px; height: 23px; }
  .f-address { left: 178px; top: 594px; width: 186px; height: 55px; }
  .f-phone { left: 379px; top: 594px; width: 185px; height: 23px; }
  .f-email { left: 379px; top: 627px; width: 185px; height: 22px; }
  .f-project { left: 178px; top: 661px; width: 386px; height: 79px; }
  .submit { position: absolute; left: 300px; top: 774px; width: 143px; height: 35px; background: var(--accent);
    border-bottom: 3px solid var(--accent-dark); border-radius: 2px; color: var(--white); font-size: 11px; font-weight: 600;
    display: flex; align-items: center; justify-content: center; }

  .footer { position: absolute; left: 0; top: 870px; width: 743px; height: 96px; background: var(--footer); color: var(--white); }
  .footer .brand { left: 100px; top: 28px; font-size: 11px; }
  .footer-phone { position: absolute; left: 102px; top: 56px; display: flex; align-items: center; gap: 5px;
    font-family: "Open Sans", sans-serif; font-weight: 700; font-size: 8.5px; }
  .to-top { position: absolute; left: 615px; top: 26px; }
  .copyright { position: absolute; right: 100px; top: 53px; font-family: "Open Sans", sans-serif; font-size: 6.5px; color: #ddd; }
</style>
</head>
<body>
  <main class="page">
    <header class="hero" role="img" aria-label="Photo of a two-storey house with a company pickup truck and work trailers parked in front, under a deep blue overlay">
      <div class="brand"><span class="brand-mark"></span>BLUEFINCH PAINTING</div>
      <ul class="nav">
        <li>Home</li><li>About</li><li>Contact</li><li>Services</li><li>Projects</li>
      </ul>
      <div class="hero-frame">GET AN ESTIMATE</div>
      <p class="hero-lead">We will provide you with a free estimated cost<br>for your house! Just fill up the form below.</p>
      <svg class="scroll-down" width="26" height="18" viewBox="0 0 26 18">
        <polyline points="1,2 13,8 25,2" fill="none" stroke="#cfd6e4" stroke-width="2.5"/>
        <polyline points="1,9 13,15 25,9" fill="none" stroke="#cfd6e4" stroke-width="2.5"/>
      </svg>
    </header>

    <section class="band">
      <h1>ESTIMATE REQUEST FORM</h1>
      <p>Tell us about the space you want painted. The more details you give, the more specific and accurate the quote will be.</p>
    </section>

    <div class="contact-row">
      <div class="dot"></div>
      <div class="dot">
        <svg width="10" height="10" viewBox="0 0 24 24"><path fill="#fff" d="M6.6 10.8a15 15 0 0 0 6.6 6.6l2.2-2.2c.3-.3.7-.4 1-.2 1.1.4 2.3.6 3.6.6.6 0 1 .4 1 1V20c0 .6-.4 1-1 1A17 17 0 0 1 3 4c0-.6.4-1 1-1h3.5c.6 0 1 .4 1 1 0 1.3.2 2.5.6 3.6.1.3 0 .7-.2 1z"/></svg>
      </div>
      <span>(555) 318-7764</span>
    </div>

    <div class="field f-name">Name</div>
    <div class="field f-address">Address</div>
    <div class="field f-phone">Phone Number</div>
    <div class="field f-email">E-mail Address</div>
    <div class="field f-project">Painting Project Description</div>
    <div class="submit">Submit</div>

    <footer class="footer">
      <div class="brand"><span class="brand-mark"></span>BLUEFINCH PAINTING</div>
      <div class="footer-phone">
        <svg width="10" height="12" viewBox="0 0 24 24"><path fill="#fff" d="M6.6 10.8a15 15 0 0 0 6.6 6.6l2.2-2.2c.3-.3.7-.4 1-.2 1.1.4 2.3.6 3.6.6.6 0 1 .4 1 1V20c0 .6-.4 1-1 1A17 17 0 0 1 3 4c0-.6.4-1 1-1h3.5c.6 0 1 .4 1 1 0 1.3.2 2.5.6 3.6.1.3 0 .7-.2 1z"/></svg>
        (555) 318-7764
      </div>
      <svg class="to-top" width="26" height="8" viewBox="0 0 26 8"><polyline points="1,7 13,1.5 25,7" fill="none" stroke="#777" stroke-width="3"/></svg>
      <p class="copyright">© 2014 Bluefinch Painting. All rights reserved.</p>
    </footer>
  </main>
</body>
</html>
```